Business Card Design

We need a business card design for a new company based in Melbourne Australia. We are financial broker in finance industry. We provide a wide range of finance solutions to our clients including home loans, commercial loans, business facilities, car loans, equipment loans, invoice finance, etc. The company name is from director's personal name. We would like to have a new company logo that includes KT.

Industry/Entity Type

Business

Contact Information for Business Card

company name: KT & Co Finance Pty Ltd
person's name: Kenneth Tollard
role: Managing Director
Mobile: 0417 638 294
fax: 03 9561 2047
Email: kenneth.tollard@ktcofinance.example
Address: Suite 4/718 Marlow Avenue Ferndale East Vic 3187
Credit Licence No.: 382917

```html
<!DOCTYPE html>
<html lang="en">
<head>
<meta charset="utf-8">
<title>KT &amp; Co Finance – Business Cards</title>
<link rel="stylesheet" href="https://fonts.googleapis.com/css2?family=Roboto+Condensed:wght@400;700&display=swap">
<style>
  :root {
    --bg: #e9eaec;
    --navy: #0a2169;
    --sky: #1ab1e6;
    --charcoal: #353535;
    --lime: #7ab833;
    --ink-dark: #2a2a2a;
    --ink-soft: #444;
    --white: #ffffff;
    --silver: linear-gradient(120deg, #d9dadc 0%, #f4f4f5 22%, #c9cacc 45%, #f7f7f8 62%, #d3d4d6 80%, #eeeeef 100%);
  }
  * { box-sizing: border-box; margin: 0; padding: 0; }
  html, body { width: 1200px; height: 753px; overflow: hidden; }
  body {
    background: var(--bg);
    font-family: "Roboto Condensed", "Arial Narrow", sans-serif;
    position: relative;
  }
  .card {
    position: absolute;
    width: 514px;
    height: 307px;
    background: var(--silver);
    box-shadow: 0 4px 12px rgba(0,0,0,.18);
    overflow: hidden;
  }
  .card--front-blue  { left: 48px;  top: 59px; }
  .card--front-green { left: 640px; top: 59px; }
  .card--back-blue   { left: 48px;  top: 398px; }
  .card--back-green  { left: 640px; top: 398px; }

  .theme-blue  { --band: var(--navy);     --accent: var(--sky);  --brand: var(--navy); }
  .theme-green { --band: var(--charcoal); --accent: var(--lime); --brand: var(--ink-dark); }

  .band {
    position: absolute; left: 0; right: 0; bottom: 0;
    background: var(--band);
    border-top: 6px solid var(--accent);
  }
  .card--front-blue .band, .card--front-green .band { top: 234px; }
  .card--back-blue .band,  .card--back-green .band  { top: 130px; border-top-width: 5px; }

  /* front */
  .brand-lockup {
    position: absolute; left: 0; right: 0; top: 92px;
    display: flex; align-items: center; justify-content: center; gap: 12px;
  }
  .brand-mark { width: 22px; height: 22px; background: var(--accent); }
  .brand-name { font-size: 31px; font-weight: 700; color: var(--brand); letter-spacing: .2px; }
  .website {
    position: absolute; left: 0; right: 0; top: 18px;
    text-align: center; color: var(--white);
    font-size: 16px; font-weight: 700; letter-spacing: .6px;
  }

  /* back */
  .company { position: absolute; left: 51px; top: 40px; font-size: 17px; font-weight: 700; color: var(--brand); }
  .person  { position: absolute; left: 51px; top: 82px; line-height: 20px; }
  .person__name  { font-size: 16px; font-weight: 700; color: var(--brand); }
  .person__title { font-size: 16px; color: var(--ink-soft); }
  .mini-brand {
    position: absolute; right: 48px; top: 46px;
    display: flex; align-items: center; gap: 8px;
  }
  .mini-brand .brand-mark { width: 14px; height: 14px; }
  .mini-brand__name { font-size: 40px; font-weight: 700; color: var(--brand); line-height: 1; }

  .contacts { position: absolute; left: 51px; top: 20px; list-style: none; color: var(--white); }
  .contacts li { display: flex; align-items: center; gap: 5px; font-size: 17px; height: 23px; }
  .contacts li.address { margin-top: 3px; }
  .contacts svg { width: 14px; height: 14px; fill: none; stroke: var(--white); stroke-width: 1.4; flex: none; }
  .licence {
    position: absolute; left: 0; right: 0; bottom: 14px;
    text-align: center; color: var(--white); font-size: 15px;
  }
</style>
</head>
<body>

<svg width="0" height="0" style="position:absolute">
  <symbol id="icon-mobile" viewBox="0 0 14 14"><rect x="3" y="1" width="8" height="12" rx="1.2"/><line x1="3" y1="10.5" x2="11" y2="10.5"/></symbol>
  <symbol id="icon-fax" viewBox="0 0 14 14"><rect x="4" y="1.5" width="6" height="4"/><rect x="1.5" y="5.5" width="11" height="6" rx="1"/><line x1="4" y1="9" x2="10" y2="9"/></symbol>
  <symbol id="icon-mail" viewBox="0 0 14 14"><rect x="1.5" y="3.5" width="11" height="7.5"/><polyline points="1.5,3.5 7,8 12.5,3.5"/></symbol>
  <symbol id="icon-home" viewBox="0 0 14 14"><polygon points="7,1.5 1,6.5 13,6.5" fill="#fff"/><rect x="2.5" y="6.5" width="9" height="6" fill="#fff"/><rect x="6" y="9" width="2" height="3.5" fill="#333" stroke="none"/></symbol>
</svg>

<section class="card card--front-blue theme-blue">
  <div class="brand-lockup"><span class="brand-mark"></span><span class="brand-name">KT &amp; Co Finance Pty Ltd</span></div>
  <div class="band"><p class="website">www.ktcofinance.example</p></div>
</section>

<section class="card card--front-green theme-green">
  <div class="brand-lockup"><span class="brand-mark"></span><span class="brand-name">KT &amp; Co Finance Pty Ltd</span></div>
  <div class="band"><p class="website">www.ktcofinance.example</p></div>
</section>

<section class="card card--back-blue theme-blue">
  <p class="company">KT &amp; Co Finance Pty Ltd</p>
  <div class="person"><p class="person__name">Kenneth Tollard</p><p class="person__title">Managing Director</p></div>
  <div class="mini-brand"><span class="brand-mark"></span><span class="mini-brand__name">KT</span></div>
  <div class="band">
    <ul class="contacts">
      <li><svg><use href="#icon-mobile"/></svg>0417 638 294</li>
      <li><svg><use href="#icon-fax"/></svg>03 9561 2047</li>
      <li><svg><use href="#icon-mail"/></svg>kenneth.tollard@ktcofinance.example</li>
      <li class="address"><svg><use href="#icon-home"/></svg>Suite 4/718 Marlow Avenue Ferndale East Vic 3187</li>
    </ul>
    <p class="licence">Credit Licence No.: 382917</p>
  </div>
</section>

<section class="card card--back-green theme-green">
  <p class="company">KT &amp; Co Finance Pty Ltd</p>
  <div class="person"><p class="person__name">Kenneth Tollard</p><p class="person__title">Managing Director</p></div>
  <div class="mini-brand"><span class="brand-mark"></span><span class="mini-brand__name">KT</span></div>
  <div class="band">
    <ul class="contacts">
      <li><svg><use href="#icon-mobile"/></svg>0417 638 294</li>
      <li><svg><use href="#icon-fax"/></svg>03 9561 2047</li>
      <li><svg><use href="#icon-mail"/></svg>kenneth.tollard@ktcofinance.example</li>
      <li class="address"><svg><use href="#icon-home"/></svg>Suite 4/718 Marlow Avenue Ferndale East Vic 3187</li>
    </ul>
    <p class="licence">Credit Licence No.: 382917</p>
  </div>
</section>

</body>
</html>
```